Lumora Dwellings

Design a stylish Business card- we would like a businness card design that suits plastic business cards. Our card needs to show that we are tech savy and technology based so the design is crucial.

Target Market(s)

22-40

Industry/Entity Type

Plastic

Requirements
Must have
• attached is our logo. also double sided card would be nice.
my details

Tobias Fenwright
Director
0471596234
www.lumoradwellings.com.au
17 Ashcombe Lane, West Perth

```html
<!DOCTYPE html>
<html lang="en">
<head>
<meta charset="utf-8">
<title>Lumora Dwellings – Business Card</title>
<link rel="stylesheet" href="https://fonts.googleapis.com/css2?family=Didact+Gothic&display=swap">
<style>
  :root {
    --backdrop: #d8d3cd;
    --card-dark: #050607;
    --card-glow: #2a8fb8;
    --frost: #e7e5e3;
    --frost-edge: #c9c6c3;
    --ink: #262626;
    --ink-soft: #5a5a5a;
    --brand-blue: #3a9cc4;
    --rule: #8a8886;
  }
  * { box-sizing: border-box; margin: 0; padding: 0; }
  html, body {
    width: 1200px; height: 900px; overflow: hidden;
    background: var(--backdrop);
    font-family: "Didact Gothic", "Century Gothic", sans-serif;
  }
  .canvas { position: relative; width: 1200px; height: 900px; }
  .card {
    position: absolute; left: 172px; top: 212px;
    width: 856px; height: 476px;
    display: flex;
    box-shadow: 0 10px 30px rgba(0,0,0,0.18);
  }
  .card-front {
    width: 404px; height: 100%;
    background: linear-gradient(to bottom, var(--card-dark) 0%, var(--card-dark) 64%, #0b1e2a 80%, var(--card-glow) 100%);
    display: flex; align-items: center; justify-content: center;
    gap: 12px;
  }
  .brand-mark {
    width: 14px; height: 14px; background: var(--brand-blue);
  }
  .brand-name {
    color: var(--brand-blue);
    font-size: 32px; letter-spacing: 1px;
  }
  .card-back {
    position: relative;
    width: 452px; height: 100%;
    background: var(--frost);
    border: 1px solid var(--frost-edge);
    border-left: none;
    color: var(--ink);
  }
  .holder { position: absolute; left: 78px; top: 142px; }
  .holder-name { font-size: 27px; letter-spacing: 0.5px; }
  .holder-role { font-size: 21px; margin-top: 6px; color: var(--ink); }
  .name-rule {
    position: absolute; left: 74px; top: 238px;
    width: 176px; height: 3px; background: var(--rule);
  }
  .contacts {
    position: absolute; left: 16px; top: 378px;
    list-style: none;
  }
  .contact {
    display: flex; align-items: center; gap: 8px;
    font-size: 21px; height: 32px;
  }
  .contact-icon {
    width: 24px; height: 24px;
    border: 1.5px solid var(--ink-soft); border-radius: 3px;
    display: flex; align-items: center; justify-content: center;
  }
  .contact-icon svg { width: 16px; height: 16px; stroke: var(--ink-soft); fill: none; stroke-width: 1.6; }
</style>
</head>
<body>
<div class="canvas">
  <div class="card">
    <section class="card-front">
      <span class="brand-mark"></span>
      <span class="brand-name">Lumora Dwellings</span>
    </section>
    <section class="card-back">
      <div class="holder">
        <p class="holder-name">Tobias Fenwright</p>
        <p class="holder-role">Director</p>
      </div>
      <div class="name-rule"></div>
      <ul class="contacts">
        <li class="contact">
          <span class="contact-icon"><svg viewBox="0 0 16 16"><rect x="4.5" y="1.5" width="7" height="13" rx="1"/><line x1="7" y1="12" x2="9" y2="12"/></svg></span>
          0471596234
        </li>
        <li class="contact">
          <span class="contact-icon"><svg viewBox="0 0 16 16"><path d="M2 8 L8 2.5 L14 8"/><path d="M4 7 V14 H12 V7"/><rect x="7" y="10" width="2" height="4"/></svg></span>
          17 Ashcombe Lane, West Perth
        </li>
        <li class="contact">
          <span class="contact-icon"><svg viewBox="0 0 16 16"><circle cx="8" cy="8" r="6"/><ellipse cx="8" cy="8" rx="2.6" ry="6"/><line x1="2" y1="8" x2="14" y2="8"/></svg></span>
          www.lumoradwellings.com.au
        </li>
      </ul>
    </section>
  </div>
</div>
</body>
</html>
```